Corvanto Card

The logo is the Spanish flag colors I want a vibrant eye catching design with the yellow / red colors over either Navy or white background or black even ,
Would like a 2D feel to the logo with another lighter color logo under it look ,

Contact Information for Business Card

Corvanto Flooring
Tobias Renwick
Main Number
Cell Number
Fax Number

Website on the side of the card somewhere

Font styles to use
Sans Serif

Colors
ec1f27
ffc214

Requirements
Must have
• 2 logos feel one is bolder and the other one underneath very light

```html
<!DOCTYPE html>
<html lang="en">
<head>
<meta charset="utf-8">
<title>Corvanto Flooring – Business Card</title>
<link rel="stylesheet" href="https://fonts.googleapis.com/css2?family=Ubuntu:wght@400;500;700&display=swap">
<style>
  :root {
    --navy: #13174a;
    --red: #ec1f27;
    --yellow: #ffc214;
    --gold: #e6b52a;
    --ink: #1d1d1f;
    --paper: #ffffff;
    --backdrop: #d9d9d9;
    --rule: #e4e4e4;
  }
  * { box-sizing: border-box; margin: 0; padding: 0; }
  html, body {
    width: 1200px; height: 900px; overflow: hidden;
    background: var(--backdrop);
    font-family: "Ubuntu", sans-serif;
  }
  .stage { position: relative; width: 1200px; height: 900px; }
  .card {
    position: absolute; width: 560px; height: 320px;
    box-shadow: 0 10px 24px rgba(0,0,0,.22);
    overflow: hidden;
  }

  /* Front */
  .card--front { left: 90px; top: 90px; background: var(--navy); }
  .front__stripes {
    position: absolute; left: 0; bottom: 0; width: 220px; height: 220px;
    background: linear-gradient(45deg, var(--yellow) 0%, var(--red) 100%);
    clip-path: polygon(0 0, 100% 100%, 0 100%);
  }
  .front__brand {
    position: absolute; left: 290px; top: 112px;
    font-weight: 500; font-size: 24px; letter-spacing: 4px;
    text-transform: uppercase; color: var(--gold); line-height: 1.1;
  }
  .front__web {
    position: absolute; left: 290px; top: 220px;
    font-size: 14px; letter-spacing: 2.5px; color: var(--red);
  }

  /* Back */
  .card--back { left: 550px; top: 470px; background: var(--paper); }
  .back__brand {
    position: absolute; left: 30px; top: 80px; width: 240px;
    display: flex; flex-direction: column; align-items: center; gap: 16px;
  }
  .back__mark { width: 56px; height: 56px; background: var(--red); }
  .back__name {
    font-weight: 500; font-size: 24px; letter-spacing: 4px; line-height: 1.1;
    text-transform: uppercase; color: var(--gold); text-align: center;
  }
  .back__divider {
    position: absolute; left: 300px; top: 40px; width: 1px; height: 240px;
    background: var(--rule);
  }
  .contact { position: absolute; left: 322px; top: 50px; width: 220px; color: var(--ink); }
  .contact__name { color: var(--red); font-weight: 700; font-size: 16px; text-transform: uppercase; }
  .contact__role { font-weight: 500; font-size: 15px; margin-bottom: 16px; }
  .contact__address { font-size: 14px; line-height: 1.3; margin-bottom: 16px; }
  .contact__list { list-style: none; font-size: 14px; }
  .contact__item { display: flex; align-items: center; gap: 8px; margin-bottom: 5px; }
  .contact__icon { width: 16px; height: 16px; flex: none; }
</style>
</head>
<body>
<main class="stage">
  <section class="card card--front" aria-label="Card front">
    <div class="front__stripes" role="img" aria-label="Red and yellow brand stripe decoration"></div>
    <div class="front__brand">Corvanto<br>Flooring</div>
    <div class="front__web">www.corvantoflooring.com</div>
  </section>

  <section class="card card--back" aria-label="Card back">
    <div class="back__brand">
      <span class="back__mark"></span>
      <span class="back__name">Corvanto<br>Flooring</span>
    </div>
    <div class="back__divider"></div>
    <div class="contact">
      <p class="contact__name">Tobias Renwick</p>
      <p class="contact__role">Director</p>
      <p class="contact__address">Suite 102 Street name, State,<br>Zip 2034, Country</p>
      <ul class="contact__list">
        <li class="contact__item">
          <svg class="contact__icon" viewBox="0 0 16 16" aria-hidden="true"><rect width="16" height="16" fill="#ec1f27"/><rect x="5" y="2.5" width="6" height="11" rx="1" fill="none" stroke="#fff" stroke-width="1.3"/><circle cx="8" cy="11.5" r=".8" fill="#fff"/></svg>
          <span>0110 111 111</span>
        </li>
        <li class="contact__item">
          <svg class="contact__icon" viewBox="0 0 16 16" aria-hidden="true"><rect width="16" height="16" fill="#ec1f27"/><path d="M3 6.5c0-2 10-2 10 0v1h-2.5V6h-5v1.5H3z" fill="#fff"/><rect x="4" y="8.5" width="8" height="4.5" rx="1" fill="#fff"/></svg>
          <span>2222 111 222</span>
        </li>
        <li class="contact__item">
          <svg class="contact__icon" viewBox="0 0 16 16" aria-hidden="true"><rect width="16" height="16" fill="#ec1f27"/><rect x="3" y="4.5" width="10" height="7" fill="none" stroke="#fff" stroke-width="1.3"/><path d="M3 4.5l5 4 5-4" fill="none" stroke="#fff" stroke-width="1.3"/></svg>
          <span>info@corvantoflooring.com</span>
        </li>
      </ul>
    </div>
  </section>
</main>
</body>
</html>
```